Corporate Branding - Web and Print

A UK based company will like to use an existing logo to create branding materials for all marketing related documents, including business card, prints, letterhead, Website, Twitter, Facebook, Instagram logo etc. This company serves high-end clientele in the fashion, health and wellness and as such high quality and class is of utmost importance.
Where the logo can be modernised without losing its character then experiment. The main thing is to have a corporate branding which can be used later for brochures, Business Plan infographics.
The prominent colour within the organisation is burnt orange with no secondary colour. However if you believe a secondary colour is needed then use it, otherwise keep it simple and classy. Any chosen colours have to match perfectly.
Target Market(s)
High net worth individuals
Industry/Entity Type
Health And Wellness
Contact Information for Business Card
classy
Look and feel
Each slider illustrates characteristics of the customer's brand and the style your logo design should communicate.

```html
<!DOCTYPE html>
<html lang="en">
<head>
<meta charset="utf-8">
<title>Veloria Business Card</title>
<link rel="stylesheet" href="https://fonts.googleapis.com/css2?family=Work+Sans:wght@400;500;700&display=swap">
<style>
  :root {
    --burnt-orange: #f39323;
    --paper: #ffffff;
    --charcoal: #2a2a2a;
    --charcoal-light: #363636;
    --ink: #555555;
    --ink-soft: #8a8a8a;
    --divider: #9a9a9a;
    --backdrop: #e4e4e4;
  }
  * { box-sizing: border-box; margin: 0; padding: 0; }
  html, body { width: 1200px; height: 1000px; overflow: hidden; }
  body {
    background: var(--backdrop);
    font-family: "Work Sans", Arial, sans-serif;
    position: relative;
  }
  .card-set {
    position: absolute;
    left: 30px; top: 340px;
    display: flex; gap: 20px;
  }
  .card {
    width: 560px; height: 320px;
    position: relative;
    box-shadow: 0 4px 14px rgba(0,0,0,0.18);
    overflow: hidden;
  }
  /* Front */
  .card-front { background: var(--paper); }
  .edge-bar {
    position: absolute; width: 8px; height: 230px; top: 45px;
    background: var(--burnt-orange);
  }
  .edge-bar--left { left: 0; }
  .edge-bar--right { right: 0; }
  .brand-block {
    position: absolute; left: 40px; top: 70px; width: 180px;
    display: flex; flex-direction: column; align-items: center; gap: 14px;
  }
  .brand-dot {
    width: 120px; height: 120px; border-radius: 50%;
    background: var(--burnt-orange);
  }
  .brand-name {
    font-weight: 700; font-size: 26px; letter-spacing: 1px;
    color: var(--burnt-orange);
  }
  .divider {
    position: absolute; left: 250px; top: 62px;
    width: 2px; height: 190px; background: var(--divider);
  }
  .contact-block { position: absolute; left: 272px; top: 64px; color: var(--ink); }
  .person-name {
    font-size: 19px; font-weight: 500; color: var(--burnt-orange);
    text-transform: uppercase; letter-spacing: 0.3px;
  }
  .person-title { font-size: 13px; color: var(--ink-soft); margin-top: 2px; }
  .address { font-size: 13px; line-height: 1.45; margin-top: 22px; }
  .contact-list { list-style: none; margin-top: 12px; font-size: 13px; line-height: 1.55; }
  .contact-list li { display: flex; align-items: center; gap: 8px; }
  .contact-list svg { width: 11px; height: 11px; fill: var(--burnt-orange); flex: none; }
  .accent { color: var(--burnt-orange); }
  /* Back */
  .card-back { background: var(--charcoal); }
  .world-map {
    position: absolute; left: 40px; top: 20px; width: 480px; height: 260px;
    background: radial-gradient(ellipse at center, var(--charcoal-light) 0%, var(--charcoal) 75%);
    border-radius: 40%;
  }
  .back-brand {
    position: absolute; left: 0; right: 0; top: 140px;
    text-align: center;
    font-weight: 700; font-size: 44px; letter-spacing: 2px;
    color: var(--burnt-orange);
  }
</style>
</head>
<body>
  <div class="card-set">
    <section class="card card-front">
      <span class="edge-bar edge-bar--left"></span>
      <span class="edge-bar edge-bar--right"></span>
      <div class="brand-block">
        <span class="brand-dot"></span>
        <span class="brand-name">VELORIA</span>
      </div>
      <span class="divider"></span>
      <div class="contact-block">
        <p class="person-name">Adrian Hale</p>
        <p class="person-title">President</p>
        <p class="address">Your Street Address,<br>Suite-111, State, Country</p>
        <ul class="contact-list">
          <li><svg viewBox="0 0 24 24"><path d="M6.6 10.8a15 15 0 0 0 6.6 6.6l2.2-2.2c.3-.3.7-.4 1-.2 1.1.4 2.3.6 3.6.6.6 0 1 .4 1 1V20c0 .6-.4 1-1 1A17 17 0 0 1 3 4c0-.6.4-1 1-1h3.5c.6 0 1 .4 1 1 0 1.3.2 2.5.6 3.6.1.3 0 .7-.2 1z"/></svg>000 000 0000</li>
          <li><svg viewBox="0 0 24 24"><path d="M2 5h20v14H2z M2 5l10 8 10-8" fill="none" stroke="#f39323" stroke-width="2.5"/></svg>info@adrianhale.com</li>
          <li><svg viewBox="0 0 24 24"><circle cx="12" cy="12" r="9" fill="none" stroke="#f39323" stroke-width="2.5"/><path d="M3 12h18M12 3c3 3 3 15 0 18M12 3c-3 3-3 15 0 18" fill="none" stroke="#f39323" stroke-width="2"/></svg>www.<span class="accent">veloria</span>.com</li>
          <li><svg viewBox="0 0 24 24"><circle cx="12" cy="8" r="4"/><path d="M4 21c0-4.4 3.6-7 8-7s8 2.6 8 7z"/></svg>adrianhale</li>
        </ul>
      </div>
    </section>
    <section class="card card-back">
      <div class="world-map" role="img" aria-label="Faint embossed world map across the card"></div>
      <p class="back-brand">VELORIA</p>
    </section>
  </div>
</body>
</html>
```